Need Eye Catching For Sale By Owner Signs

In need of a Eye Catching For Sale By Owner Sign design. I plan on using the sign to market buildings and raw land that I own. The design should be able to scale to different rectangular dimensions for example a yard stake sign or a large 4' x 6' sign to be tacked to plywood. The design should have a dead space near the bottom that I can insert more detail information into at a later time.

The main tag line "For Sale By Owner" and the contact number "318-562-4097" needs to be easily be read from a distance.

```html
<!DOCTYPE html>
<html lang="en">
<head>
<meta charset="utf-8">
<title>For Sale By Owner Sign</title>
<link rel="stylesheet" href="https://fonts.googleapis.com/css2?family=Anton&display=swap">
<style>
  :root {
    --sign-red: #d9261c;
    --outline-white: #ffffff;
    --panel-white: #ffffff;
    --backdrop-light: #f7f7f7;
    --backdrop-edge: #d9d9d9;
    --shadow-grey: rgba(0, 0, 0, 0.28);
  }
  html, body {
    margin: 0;
    padding: 0;
    width: 1200px;
    height: 799px;
    overflow: hidden;
    background: #ffffff;
  }
  .sign {
    position: relative;
    width: 1200px;
    height: 799px;
    box-sizing: border-box;
    border: 14px solid #ffffff;
    background: radial-gradient(ellipse at 50% 40%, var(--backdrop-light) 0%, #ececec 70%, var(--backdrop-edge) 100%);
  }
  .headline {
    position: absolute;
    left: 0;
    top: 0;
    width: 1200px;
    height: 799px;
  }
  .headline-line {
    font-family: "Anton", "Impact", sans-serif;
    fill: var(--sign-red);
    stroke: var(--outline-white);
    stroke-width: 6px;
    stroke-linejoin: round;
    paint-order: stroke fill;
    filter: drop-shadow(2px 3px 3px var(--shadow-grey));
  }
  .headline-line--top { font-size: 274px; }
  .headline-line--bottom { font-size: 256px; }
  .info-panel {
    position: absolute;
    left: 42px;
    top: 533px;
    width: 1119px;
    height: 222px;
    background: var(--panel-white);
    border-radius: 18px;
    box-shadow: 0 0 3px rgba(0, 0, 0, 0.08);
  }
</style>
</head>
<body>
  <main class="sign">
    <svg class="headline" viewBox="0 0 1200 799" aria-labelledby="headline-text">
      <title id="headline-text">For Sale By Owner</title>
      <text class="headline-line headline-line--top" x="36" y="267" textLength="1128" lengthAdjust="spacingAndGlyphs">FOR SALE</text>
      <text class="headline-line headline-line--bottom" x="36" y="507" textLength="1135" lengthAdjust="spacingAndGlyphs">BY OWNER</text>
    </svg>
    <div class="info-panel"></div>
  </main>
</body>
</html>
```